KVT Wellness Co Business Card for food and Beverage Falcons & Lanterns

One main business card design for a wellness enterprise which represents two brands. We need one primary card design, for two different employees. The only difference between the cards will be the name, title and phone number for each employee, all other design elements will be same.
I've uploaded the logos for each brand. I have also uploaded a mockup which I made using Google's drawing tool. I can provide example images of business cards we find attractive if you would like some help picturing what we like.
I'm picturing the color splash on the back of the card below the two logos to be a dark burgundy or blue. This may sound a bit silly but the feel of the card and color should look almost like wizard dress robes. Dark emerald green, dark blue and dark burgundy with black undertones and gold lace.
Updates

Reason: Thank you all for the submissions. I will need some extra time to give you feedback. Cheers

Target Market(s)

Healthy food and beverage industry

Industry/Entity Type

Health And Wellness

Contact Information for Business Card

On one side we would like the business name, location, title of employee, employee name and contact details. On the flip side we would like our two brand logos and a splash of color. We would like the card to have a black font with some gold accents if possible. We would also like the trim of the business card or a middle ply within the card stock to have a color other than white.

Font styles to use
Serif

Colors
ec1f27
0255a3
00a990

Requirements
Must have
• Bold dark colors, happy to provide sample photos of business cards I like from clipnook. Must have a version for two different employees. Must be sharp, modern and chic.
Nice to have
• Thick card stock layer in between the front and back of card that is either black or gold lace or something to make it feel, well let's say to make it feel expensive.
Should not have
• Should not have any cartoon-ey elements. All business.

```html
<!DOCTYPE html>
<html lang="en">
<head>
<meta charset="UTF-8">
<title>KVT Wellness Co Business Card</title>
<link rel="stylesheet" href="https://fonts.googleapis.com/css2?family=Roboto:wght@400;500&display=swap">
<style>
  :root {
    --backdrop: #e9dccb;
    --card-black: #050505;
    --card-white: #f7f6f3;
    --gold: #c9a646;
    --gold-deep: #8f7228;
    --gold-light: #e4cb7a;
    --title-grey: #c9c9c9;
    --contact-white: #e6e6e6;
    --ink: #111111;
    --edge-gold: #b8913f;
  }
  * { box-sizing: border-box; margin: 0; padding: 0; }
  html, body {
    width: 1200px;
    height: 800px;
    overflow: hidden;
    background: var(--backdrop);
    font-family: "Roboto", Arial, sans-serif;
  }
  .sheet {
    position: relative;
    width: 1200px;
    height: 800px;
    display: flex;
    align-items: center;
    justify-content: center;
    gap: 40px;
  }
  .card {
    position: relative;
    width: 540px;
    height: 308px;
    border-radius: 4px;
    overflow: hidden;
    box-shadow: 0 0 0 3px var(--edge-gold), 0 10px 24px rgba(60, 40, 20, 0.25);
  }
  /* Front */
  .card-front { background: var(--card-black); }
  .lace-band {
    position: absolute;
    left: 0;
    width: 100%;
    height: 34px;
    background: linear-gradient(180deg, var(--gold-deep) 0%, var(--gold-light) 45%, var(--gold) 70%, var(--gold-deep) 100%);
  }
  .lace-band.top { top: 22px; }
  .lace-band.bottom { bottom: 22px; }
  .front-content {
    position: absolute;
    top: 50%;
    left: 0;
    width: 100%;
    transform: translateY(-50%);
    display: flex;
    align-items: center;
    justify-content: center;
  }
  .identity { text-align: right; padding-right: 12px; }
  .person-name {
    color: var(--gold);
    font-size: 21px;
    font-weight: 500;
    letter-spacing: 0.5px;
  }
  .person-title {
    color: var(--title-grey);
    font-size: 17px;
    font-weight: 400;
    margin-top: 1px;
  }
  .divider {
    width: 1.5px;
    height: 46px;
    background: var(--gold);
    align-self: flex-end;
    margin-bottom: -18px;
  }
  .contact {
    padding-left: 12px;
    color: var(--contact-white);
    font-size: 14px;
    line-height: 1.6;
    align-self: flex-end;
    margin-bottom: -40px;
  }
  /* Back */
  .card-back {
    background: var(--card-white);
    display: flex;
    align-items: center;
    justify-content: space-around;
    padding: 0 30px;
  }
  .brand {
    display: flex;
    align-items: center;
    gap: 8px;
    color: var(--ink);
    font-size: 20px;
    font-weight: 500;
  }
  .brand-dot {
    width: 10px;
    height: 10px;
    background: var(--ink);
    border-radius: 50%;
  }
</style>
</head>
<body>
<main class="sheet">
  <section class="card card-front">
    <div class="lace-band top" role="img" aria-label="Gold lace border"></div>
    <div class="front-content">
      <div class="identity">
        <p class="person-name">Miles Harlan</p>
        <p class="person-title">Beverage Alchemist</p>
      </div>
      <div class="divider"></div>
      <div class="contact">
        <p class="phone">415.555.0142</p>
        <p class="email">kvtwellnessco@example.com</p>
      </div>
    </div>
    <div class="lace-band bottom" role="img" aria-label="Gold lace border"></div>
  </section>

  <section class="card card-back">
    <div class="brand brand-secondary">Falcons &amp; Lanterns</div>
    <div class="brand brand-primary"><span class="brand-dot"></span>KVT Wellness Co</div>
  </section>
</main>
</body>
</html>
```